Craft Beer Needs a Label/ Logo Design

Name: Lanternfall
(Lanternfall Ale, Lanternfall Pilsner, Lanternfall Stout)

We are looking for a logo-ed label that will resonate domestically and internationally for this new Craft Beer Brand.

Target Market(s)

Millenials

Logo Text

Lanternfall Pilsner

Logo styles of interest
Emblem Logo
Character Logo
Colors

Designer to choose colors to be used in the design.

Requirements
Must have
• A labled logo design -- "Lanternfall" is the name, but would like to see samples with "Ale", "Pilsner", or "Stout" after!

```html
<!DOCTYPE html>
<html lang="en">
<head>
<meta charset="utf-8">
<title>Lanternfall Ale Label</title>
<link rel="stylesheet" href="https://fonts.googleapis.com/css2?family=Cinzel:wght@700&family=Montserrat:wght@300;600&display=swap">
<style>
  :root {
    --backdrop: #ececea;
    --label-black: #151515;
    --gold: #c8b98c;
    --gold-light: #ddd2ad;
    --gold-dark: #9c8d62;
  }
  html, body {
    margin: 0;
    padding: 0;
    width: 816px;
    height: 1200px;
    overflow: hidden;
    background: var(--backdrop);
  }
  .canvas {
    position: relative;
    width: 816px;
    height: 1200px;
  }
  .label {
    position: absolute;
    left: 148px;
    top: 150px;
    width: 520px;
    height: 900px;
    background: var(--label-black);
    box-sizing: border-box;
  }
  .frame-outer,
  .frame-inner {
    position: absolute;
    border: 2px solid var(--gold);
    pointer-events: none;
  }
  .frame-outer { inset: 14px; }
  .frame-inner { inset: 24px; border-width: 1px; }
  .brand-name {
    position: absolute;
    top: 92px;
    left: 0;
    right: 0;
    margin: 0;
    text-align: center;
    font-family: "Cinzel", serif;
    font-weight: 700;
    font-size: 44px;
    letter-spacing: 1px;
    color: var(--gold);
  }
  .beer-style {
    position: absolute;
    top: 162px;
    left: 60px;
    right: 60px;
    margin: 0;
    display: flex;
    justify-content: space-between;
    font-family: "Montserrat", sans-serif;
    font-weight: 300;
    font-size: 22px;
    color: var(--gold);
  }
  .emblem {
    position: absolute;
    left: 70px;
    top: 330px;
    width: 380px;
    height: 380px;
  }
  .emblem-name {
    position: absolute;
    left: 0;
    right: 0;
    top: 502px;
    margin: 0;
    text-align: center;
    font-family: "Cinzel", serif;
    font-weight: 700;
    font-size: 34px;
    color: var(--label-black);
  }
  .vintage {
    position: absolute;
    bottom: 54px;
    left: 0;
    right: 0;
    margin: 0;
    text-align: center;
    font-family: "Montserrat", sans-serif;
    font-weight: 600;
    font-size: 26px;
    letter-spacing: 1px;
    color: var(--gold);
  }
</style>
</head>
<body>
<main class="canvas">
  <section class="label" aria-label="Lanternfall Ale bottle label">
    <div class="frame-outer"></div>
    <div class="frame-inner"></div>
    <h1 class="brand-name">LANTERNFALL</h1>
    <p class="beer-style"><span>A</span><span>L</span><span>E</span></p>
    <svg class="emblem" viewBox="0 0 380 380" aria-hidden="true">
      <defs>
        <radialGradient id="gold-disc" cx="45%" cy="40%" r="65%">
          <stop offset="0%" stop-color="var(--gold-light)"/>
          <stop offset="100%" stop-color="var(--gold-dark)"/>
        </radialGradient>
      </defs>
      <circle cx="190" cy="190" r="150" fill="url(#gold-disc)"/>
    </svg>
    <p class="emblem-name">LANTERNFALL</p>
    <p class="vintage">2014</p>
  </section>
</main>
</body>
</html>
```